Business cards for a high-end menswear store

I would like to come up with a design for our business cards.
Two different ones: one for general sales and one for the owner. It is a high-end menswear store.

Our address is: 4817 Morneau Boulevard, Montreal, QC, K7P4M2
phone number: 514-286-5937
insta: MAISONVERLAINE
Website: www.maisonverlaine.example
email (general card): info@maisonverlaine.example
email (owner): bastien@maisonverlaine.example

I have attached our logo in an ai and eps file format. You can see our old cards as well. I am looking for a modern and clean look.

Target Market(s)

High-End Clothing Market

Industry/Entity Type

Retail, Clothing, Luxury Clothing

Contact Information for Business Card

Address, Name, Email, Website, Social Info,

Font styles to use
Serif

Colors

Designer to choose colors to be used in the design.

Requirements
Must have
• Address, Name, Email, Website, Social Info,
Nice to have
• QR Code that brings you to the website

```html
<!DOCTYPE html>
<html lang="en">
<head>
<meta charset="utf-8">
<title>Maison Verlaine — Business Cards</title>
<link rel="stylesheet" href="https://fonts.googleapis.com/css2?family=Roboto:wght@400;700&family=Rubik:wght@400&display=swap">
<style>
  :root {
    --backdrop: #7b7b7b;
    --paper: #ffffff;
    --ink: #030303;
    --bar: #222121;
    --text-light: #ffffff;
    --text-muted: #e6e6e6;
  }
  * { margin: 0; padding: 0; box-sizing: border-box; }
  html, body {
    width: 1200px; height: 1200px; overflow: hidden;
    background: var(--backdrop);
  }
  .canvas { position: relative; width: 1200px; height: 1200px; }

  .card {
    position: absolute; left: 237px; width: 726px; height: 402px;
    background: var(--paper); overflow: hidden;
  }
  .card--front { top: 150px; }
  .card--back  { top: 648px; }

  .brand {
    position: absolute; display: flex; align-items: center; gap: 12px;
    white-space: nowrap;
  }
  .brand-mark { width: 14px; height: 14px; background: var(--ink); flex: none; }
  .brand-name {
    font-family: "Roboto", sans-serif; font-weight: 700;
    color: var(--ink); line-height: 1;
  }

  .card--front .brand { left: 0; right: 0; top: 182px; justify-content: center; }
  .card--front .brand-name { font-size: 38px; }

  .side-bar { position: absolute; width: 40px; height: 61px; background: var(--bar); }
  .side-bar--left  { left: 0; }
  .side-bar--right { right: 0; }
  .side-bar--upper { top: 110px; }
  .side-bar--lower { top: 232px; }

  .card--back .brand { left: 58px; top: 190px; gap: 9px; }
  .card--back .brand .brand-mark { width: 11px; height: 11px; }
  .card--back .brand-name { font-size: 27px; }

  .contact-panel {
    position: absolute; inset: 0; background: var(--ink);
    clip-path: polygon(370px 0, 726px 0, 726px 402px, 320px 402px);
  }
  .person-name {
    position: absolute; left: 406px; top: 44px;
    font-family: "Roboto", sans-serif; font-weight: 700;
    font-size: 31px; color: var(--text-light); letter-spacing: 0.2px;
  }
  .person-role {
    position: absolute; left: 406px; top: 79px;
    font-family: "Roboto", sans-serif; font-weight: 400;
    font-size: 18px; color: var(--text-muted);
  }
  .contact-item {
    position: absolute; display: flex; align-items: center;
    font-family: "Rubik", sans-serif; font-size: 18px;
    color: var(--text-light); line-height: 1.45; white-space: nowrap;
  }
  .contact-item .icon { width: 22px; height: 22px; flex: none; }
  .contact-phone   { left: 391px; top: 150px; gap: 13px; }
  .contact-email   { left: 384px; top: 189px; gap: 14px; }
  .contact-social  { left: 379px; top: 229px; gap: 16px; }
  .contact-web     { left: 374px; top: 268px; gap: 21px; }
  .contact-address { left: 369px; top: 307px; gap: 23px; }
  .contact-address .icon { width: 20px; height: 26px; }
</style>
</head>
<body>
<div class="canvas">
  <svg width="0" height="0" style="position:absolute">
    <defs>
      <linearGradient id="gold" x1="0" y1="0" x2="1" y2="1">
        <stop offset="0" stop-color="#f7dc83"/>
        <stop offset="1" stop-color="#c48f25"/>
      </linearGradient>
    </defs>
  </svg>

  <section class="card card--front" aria-label="Card front">
    <div class="side-bar side-bar--left side-bar--upper"></div>
    <div class="side-bar side-bar--left side-bar--lower"></div>
    <div class="side-bar side-bar--right side-bar--upper"></div>
    <div class="side-bar side-bar--right side-bar--lower"></div>
    <div class="brand">
      <span class="brand-mark"></span>
      <span class="brand-name">Maison Verlaine</span>
    </div>
  </section>

  <section class="card card--back" aria-label="Card back">
    <div class="brand">
      <span class="brand-mark"></span>
      <span class="brand-name">Maison Verlaine</span>
    </div>
    <div class="contact-panel"></div>

    <div class="person-name">NAME SURNAME</div>
    <div class="person-role">Job Position</div>

    <div class="contact-item contact-phone">
      <svg class="icon" viewBox="0 0 24 24"><path fill="url(#gold)" d="M6.6 3.2l2.6 3.4c.4.5.3 1.2-.1 1.6L7.6 9.6c1 2.6 3.6 5.3 6.3 6.6l1.5-1.5c.4-.4 1.1-.5 1.6-.1l3.4 2.6c.5.4.6 1.1.2 1.6l-1.6 2c-.6.7-1.6 1-2.5.7C10 19.4 4.9 14.4 2.7 8.4c-.3-.9 0-1.9.7-2.5l2-1.6c.4-.4 1-.3 1.2-.1z"/></svg>
      <span>514 286 5937</span>
    </div>
    <div class="contact-item contact-email">
      <svg class="icon" viewBox="0 0 24 24"><rect x="2" y="5" width="20" height="14" fill="none" stroke="url(#gold)" stroke-width="2"/><path d="M2 5l10 8 10-8M2 19l7.5-7M22 19l-7.5-7" fill="none" stroke="url(#gold)" stroke-width="1.8"/></svg>
      <span>info@maisonverlaine.example</span>
    </div>
    <div class="contact-item contact-social">
      <svg class="icon" viewBox="0 0 24 24"><circle cx="12" cy="12" r="9" fill="none" stroke="url(#gold)" stroke-width="2.2"/></svg>
      <span>@Maisonverlaine</span>
    </div>
    <div class="contact-item contact-web">
      <svg class="icon" viewBox="0 0 24 24"><g fill="none" stroke="url(#gold)" stroke-width="2.4" stroke-linecap="round"><path d="M10 14l-3 3a3 3 0 01-4-4l3-3a3 3 0 014 0"/><path d="M14 10l3-3a3 3 0 014 4l-3 3a3 3 0 01-4 0"/><path d="M9 15l6-6"/></g></svg>
      <span>www.maisonverlaine.example</span>
    </div>
    <div class="contact-item contact-address">
      <svg class="icon" viewBox="0 0 20 26"><path fill="url(#gold)" d="M10 0a9 9 0 00-9 9c0 6.5 9 17 9 17s9-10.5 9-17a9 9 0 00-9-9zm0 12.5A3.5 3.5 0 1110 5.5a3.5 3.5 0 010 7z"/></svg>
      <span>4817 Morneau Boulevard<br>Montreal, QC, K7P4M2</span>
    </div>
  </section>
</div>
</body>
</html>
```